Real Estate Entrepreneur needs a business card

I am a real estate entrepreneur, I buy houses for investment purposes, I act as a real estate agent representing buyers and sellers in residential home transactions, I am a contractor that does a wide range of home repairs and construction. I'd like a design that can stick with me through the years as my business grows and morphs to fit any niche I decide to pursue as markets change.

Target Market(s)

Anyone with interest that may be related to real estate.

Industry/Entity Type

Real Estate

Contact Information for Business Card

A card that stands out and doesn't put me in any one box. My business will evolve over time and I need a card that can stay relevant.

Colors

Designer to choose colors to be used in the design.

Requirements
Must have
• Character
Nice to have
• I'm open
Should not have
• Cliche houses and hammers

```html
<!DOCTYPE html>
<html lang="en">
<head>
<meta charset="UTF-8">
<title>Mark Dalton – Business Card</title>
<link rel="stylesheet" href="https://fonts.googleapis.com/css2?family=Montserrat:wght@300;400;500;600&display=swap">
<style>
  :root {
    --backdrop: #262626;
    --card: #3a3330;
    --card-edge: #302a28;
    --ink: #f4f2f0;
    --ink-soft: #d9d5d2;
  }
  * { box-sizing: border-box; margin: 0; padding: 0; }
  html, body {
    width: 1200px;
    height: 715px;
    overflow: hidden;
    background: var(--backdrop);
    font-family: "Montserrat", sans-serif;
  }
  .canvas {
    position: relative;
    width: 1200px;
    height: 715px;
  }
  .card {
    position: absolute;
    top: 214px;
    width: 500px;
    height: 286px;
    background: var(--card);
    border: 1px solid var(--card-edge);
    color: var(--ink);
  }
  .card--front { left: 60px; }
  .card--back { left: 640px; }

  .front-identity {
    position: absolute;
    left: 50%;
    top: 50%;
    transform: translate(-50%, -50%);
  }
  .front-name {
    font-weight: 600;
    font-size: 34px;
    letter-spacing: 0.5px;
    line-height: 1;
  }
  .front-role {
    margin-top: 8px;
    margin-left: 22px;
    font-weight: 300;
    font-size: 13px;
    letter-spacing: 0.6px;
    color: var(--ink-soft);
  }

  .back-block {
    position: absolute;
    left: 150px;
    top: 50%;
    transform: translateY(-50%);
    display: flex;
    align-items: center;
    gap: 14px;
  }
  .back-identity { text-align: right; }
  .back-name {
    font-weight: 600;
    font-size: 17px;
    line-height: 1.1;
  }
  .back-role {
    font-weight: 300;
    font-size: 11px;
    color: var(--ink-soft);
  }
  .back-divider {
    width: 1px;
    height: 64px;
    background: var(--ink);
  }
  .back-contact {
    list-style: none;
    font-weight: 400;
    font-size: 12px;
    letter-spacing: 0.4px;
    line-height: 1.9;
  }
  .back-contact .label { margin-right: 6px; }
</style>
</head>
<body>
  <main class="canvas">
    <section class="card card--front">
      <div class="front-identity">
        <h1 class="front-name">Mark Dalton</h1>
        <p class="front-role">Real Estate</p>
      </div>
    </section>

    <section class="card card--back">
      <div class="back-block">
        <div class="back-identity">
          <p class="back-name">Mark Dalton</p>
          <p class="back-role">Agent</p>
        </div>
        <span class="back-divider"></span>
        <ul class="back-contact">
          <li><span class="label">M :</span>99 48 215 07 36</li>
          <li><span class="label">E :</span>mark.d@dltnhome.com</li>
        </ul>
      </div>
    </section>
  </main>
</body>
</html>
```